Business Card Design

New business card design

Target Market(s)

Residential & Commercial Property Managers

Industry/Entity Type

Plumbing Services

Contact Information for Business Card

Name - Owen Tredgold, title - Director, Phone Number - 0431 862 507, email - owen@rvb-plumbing.com.au, Company ABN - 73 215 904 386,

Font styles to use
Sans Serif

Colors
0054AA
0677BA
7BADD7
CADEEF
E8F1F8

```html
<!DOCTYPE html>
<html lang="en">
<head>
<meta charset="utf-8">
<title>RVB Plumbing Services – Business Card</title>
<link rel="stylesheet" href="https://fonts.googleapis.com/css2?family=Montserrat:wght@700&family=Roboto:wght@300;400&display=swap">
<style>
  :root {
    --backdrop: #b4b4b4;
    --card-dark: #1f242a;
    --card-light: #ffffff;
    --accent: #14a3e6;
    --ink-light: #ffffff;
    --ink-dark: #1f242a;
  }
  * { box-sizing: border-box; margin: 0; padding: 0; }
  html, body { width: 1200px; height: 1015px; overflow: hidden; }
  body {
    background: var(--backdrop);
    font-family: "Roboto", sans-serif;
    display: flex;
    flex-direction: column;
    align-items: center;
    justify-content: center;
    gap: 60px;
  }
  .card {
    width: 620px;
    height: 344px;
    position: relative;
    overflow: hidden;
    box-shadow: 0 6px 18px rgba(0,0,0,.25);
  }
  .card--front {
    background: var(--card-dark);
    display: flex;
    align-items: center;
    justify-content: center;
  }
  .brand-name {
    font-family: "Roboto", sans-serif;
    font-weight: 300;
    font-size: 30px;
    letter-spacing: 0.06em;
    display: flex;
    align-items: center;
    gap: 12px;
  }
  .brand-name__dot {
    width: 14px; height: 14px; border-radius: 50%;
    background: var(--accent);
    flex: none;
  }
  .card--front .brand-name { color: var(--ink-light); }

  .card--back { display: flex; background: var(--card-dark); }
  .back__brand {
    width: 300px;
    background: var(--card-light);
    border-right: 4px solid var(--accent);
    display: flex;
    align-items: center;
    justify-content: center;
  }
  .back__brand .brand-name { color: var(--ink-dark); font-size: 21px; gap: 9px; }
  .back__brand .brand-name__dot { width: 11px; height: 11px; }
  .divider-dot {
    position: absolute;
    left: 289px; top: 62px;
    width: 22px; height: 22px; border-radius: 50%;
    background: var(--accent);
  }
  .back__details {
    flex: 1;
    padding: 52px 0 0 42px;
    color: var(--ink-light);
  }
  .person__name {
    font-family: "Montserrat", sans-serif;
    font-weight: 700;
    font-size: 19px;
    letter-spacing: 0.02em;
    text-transform: uppercase;
  }
  .person__title { font-weight: 300; font-size: 15px; margin-top: 2px; }
  .contact { list-style: none; margin-top: 30px; }
  .contact__item {
    display: flex; align-items: center; gap: 10px;
    font-weight: 300; font-size: 14px; line-height: 22px;
  }
  .contact__item svg { width: 15px; height: 15px; flex: none; }
  .abn { margin-top: 38px; font-weight: 300; font-size: 14px; }
</style>
</head>
<body>
  <section class="card card--front" aria-label="Card front">
    <div class="brand-name"><span class="brand-name__dot"></span>RVB Plumbing Services</div>
  </section>

  <section class="card card--back" aria-label="Card back">
    <div class="back__brand">
      <div class="brand-name"><span class="brand-name__dot"></span>RVB Plumbing Services</div>
    </div>
    <span class="divider-dot"></span>
    <div class="back__details">
      <p class="person__name">Owen Tredgold</p>
      <p class="person__title">Director</p>
      <ul class="contact">
        <li class="contact__item">
          <svg viewBox="0 0 16 16" aria-hidden="true"><path fill="var(--accent)" d="M3.6 1.5l2.3 2.6-1.3 1.7c.9 1.9 2.2 3.2 4.1 4.1l1.7-1.3 2.6 2.3-1.4 2.3c-5.2-.4-9.4-4.6-9.8-9.8z"/></svg>
          0431 862 507
        </li>
        <li class="contact__item">
          <svg viewBox="0 0 16 16" aria-hidden="true"><rect x="1" y="3.5" width="14" height="9" fill="var(--accent)"/><path d="M1 3.5l7 5.5 7-5.5" fill="none" stroke="var(--card-dark)" stroke-width="1.2"/></svg>
          owen@rvb-plumbing.com.au
        </li>
      </ul>
      <p class="abn">Company ABN - 73 215 904 386</p>
    </div>
  </section>
</body>
</html>
```